Report Cover

This is for a Binder Front, Side, Back. I have uploaded a few examples. We are an education resource company that delivers data in a format that allows districts to make better decisions. Our color palette is uploaded as well.

```html
<!DOCTYPE html>
<html lang="en">
<head>
<meta charset="utf-8">
<title>Comprehensive Needs Assessment – Report Cover</title>
<link rel="stylesheet" href="https://fonts.googleapis.com/css2?family=Oswald:wght@500;700&display=swap">
<style>
  :root {
    --page-bg: #f4f4f7;
    --cover-outer: #2a2278;
    --cover-inner: #1b1260;
    --gold: #f8ca6b;
    --teal: #58c4b1;
    --lavender-light: #ebebfb;
    --lavender: #d8d8f6;
    --white: #ffffff;
    --glow: #3fe0e0;
  }
  * { margin: 0; padding: 0; box-sizing: border-box; }
  html, body {
    width: 1200px; height: 1200px; overflow: hidden;
    background: var(--page-bg);
  }
  .cover {
    position: absolute; left: 176px; top: 20px;
    width: 848px; height: 1160px;
    background: linear-gradient(160deg, #2c2580 0%, var(--cover-outer) 50%, #2b2a82 100%);
    overflow: hidden;
  }
  .cover-panel {
    position: absolute; left: 58px; top: 61px; right: 60px; bottom: 60px;
    background: linear-gradient(180deg, #1a105a 0%, #1f1666 55%, #22196c 100%);
  }
  .brand {
    position: absolute; left: 500px; top: 108px;
    display: flex; align-items: center; gap: 12px;
    font-family: "Oswald", sans-serif; font-weight: 500;
    color: var(--white); font-size: 30px; line-height: 1.1;
  }
  .brand-dot {
    width: 40px; height: 40px; border-radius: 50%;
    border: 4px solid var(--white); flex: none;
  }
  .report-type {
    position: absolute; left: 88px; top: 180px;
    font-family: "Oswald", sans-serif; font-weight: 500;
    font-size: 54px; line-height: 56px; letter-spacing: -0.5px;
    color: var(--gold); text-transform: uppercase;
  }
  .illustration {
    position: absolute; left: 58px; top: 318px;
    width: 730px; height: 470px;
    background: radial-gradient(ellipse at 58% 45%, #bdbcf0 0%, #7b78d6 22%, #3a2f95 45%, rgba(34,25,108,0) 72%);
  }
  .illustration-glow {
    position: absolute; left: 58px; top: 690px; width: 730px; height: 120px;
    background: radial-gradient(ellipse at 40% 50%, rgba(63,224,224,0.22) 0%, rgba(63,224,224,0) 70%);
  }
  .district {
    position: absolute; right: 103px;
    font-family: "Oswald", sans-serif; font-weight: 700;
    text-transform: uppercase; text-align: right; white-space: nowrap;
    line-height: 1;
  }
  .district-name { top: 768px; font-size: 118px; color: var(--teal); letter-spacing: -1px; }
  .district-type { top: 878px; font-size: 86px; color: var(--lavender-light); letter-spacing: -1px; }
  .report-year { top: 956px; font-size: 142px; color: var(--lavender); letter-spacing: -2px; }
</style>
</head>
<body>
  <main class="cover">
    <div class="cover-panel"></div>

    <div class="brand">
      <span class="brand-dot"></span>
      <span class="brand-name">Brightpath<br>Learning, LLC</span>
    </div>

    <h2 class="report-type">Comprehensive<br>Needs Assessment</h2>

    <div class="illustration-glow"></div>
    <div class="illustration" role="img" aria-label="Isometric illustration of a laptop with a bar chart, a magnifying glass and a printed data report, surrounded by glowing circuit lines"></div>

    <h1 class="district district-name">Maplebrook</h1>
    <p class="district district-type">School District</p>
    <p class="district report-year">2025</p>
  </main>
</body>
</html>
```